PlumVerse Business Cards

I need a business card designed for PlumVerse. To get an idea of what we do please visit https://brisklayout.example/para-artistas-7

```html
<!DOCTYPE html>
<html lang="en">
<head>
<meta charset="UTF-8">
<title>PlumVerse Business Cards</title>
<link href="https://fonts.googleapis.com/css2?family=Montserrat:wght@400;500&family=Arimo:wght@400;700&display=swap" rel="stylesheet">
<style>
  :root {
    --backdrop: #2a2a2c;
    --card-dark: #1c1e22;
    --card-light: #ffffff;
    --accent: #e4941c;
    --ink-light: #ffffff;
    --ink-dark: #1c1e22;
  }
  * { margin: 0; padding: 0; box-sizing: border-box; }
  html, body {
    width: 1200px; height: 1015px; overflow: hidden;
    background: var(--backdrop);
  }
  .stage {
    position: relative; width: 1200px; height: 1015px;
    display: flex; flex-direction: column; align-items: center; justify-content: center; gap: 60px;
  }
  .card {
    position: relative; width: 700px; height: 400px; overflow: hidden;
    background: var(--card-dark);
    box-shadow: 0 18px 40px rgba(0,0,0,0.55);
  }
  .accent-band {
    position: absolute; left: 0; right: 0; top: 268px; height: 52px;
    background: var(--accent);
    display: flex; align-items: center; justify-content: center;
  }
  .band-url {
    font-family: "Arimo", Arial, sans-serif; font-size: 20px; letter-spacing: 1px;
    color: var(--ink-light);
  }
  .wordmark {
    display: flex; align-items: center; gap: 18px;
  }
  .wordmark-square {
    width: 26px; height: 26px; background: var(--accent);
  }
  .wordmark-name {
    font-family: "Montserrat", Arial, sans-serif; font-weight: 400;
    font-size: 38px; letter-spacing: 10px;
  }
  /* front */
  .card-front .wordmark { position: absolute; left: 0; right: 0; top: 110px; justify-content: center; }
  .card-front .wordmark-name { color: var(--ink-light); }
  .card-front .band-url { margin-left: 60px; }
  /* back */
  .card-back .light-panel {
    position: absolute; left: 0; top: 0; bottom: 0; width: 350px;
    background: var(--card-light);
  }
  .card-back .wordmark {
    position: absolute; left: 0; width: 350px; top: 110px;
    flex-direction: column; gap: 22px;
  }
  .card-back .wordmark-name { color: var(--ink-dark); font-size: 32px; letter-spacing: 8px; }
  .card-back .accent-band { justify-content: flex-start; padding-left: 320px; }
  .contact {
    position: absolute; left: 390px; top: 40px; right: 30px;
    font-family: "Arimo", Arial, sans-serif; color: var(--ink-light);
  }
  .contact-name { color: var(--accent); font-weight: 700; font-size: 24px; line-height: 1; }
  .contact-role { font-size: 17px; margin-top: 4px; }
  .contact-lines { margin-top: 22px; list-style: none; font-size: 16px; line-height: 1.5; }
  .contact-lines li { display: flex; align-items: center; gap: 8px; }
  .contact-lines svg { width: 16px; height: 16px; flex: none; }
  .contact-address { margin-top: 16px; font-size: 16px; line-height: 1.35; }
</style>
</head>
<body>
<main class="stage">
  <section class="card card-front" aria-label="Card front">
    <div class="wordmark">
      <span class="wordmark-square"></span>
      <span class="wordmark-name">PLUMVERSE</span>
    </div>
    <div class="accent-band"><span class="band-url">www.plumverse.example</span></div>
  </section>

  <section class="card card-back" aria-label="Card back">
    <div class="light-panel"></div>
    <div class="wordmark">
      <span class="wordmark-square"></span>
      <span class="wordmark-name">PLUMVERSE</span>
    </div>
    <div class="contact">
      <p class="contact-name">MARCUS ELLERY</p>
      <p class="contact-role">Managing Director</p>
      <ul class="contact-lines">
        <li>
          <svg viewBox="0 0 16 16"><path d="M4 1.5 6.5 5 5 6.5c.8 1.8 2.6 3.6 4.5 4.5L11 9.5l3.5 2.5-1.5 2.5C7.5 14.5 1.5 8.5 1.5 3z" fill="none" stroke="#e4941c" stroke-width="1.6" stroke-linejoin="round"/></svg>
          044-555 018 240
        </li>
        <li>
          <svg viewBox="0 0 16 16"><rect x="1" y="3" width="14" height="10" fill="#e4941c"/><path d="M1 3l7 6 7-6" fill="none" stroke="#1c1e22" stroke-width="1.2"/></svg>
          hello@plumverse.example
        </li>
      </ul>
      <p class="contact-address">88, Orchard Lane Studio<br>10234, Northland</p>
    </div>
    <div class="accent-band"><span class="band-url">www.plumverse.example</span></div>
  </section>
</main>
</body>
</html>
```